Zielgruppe
Unsere Vorstellung währe eine Flyer Falzflyer DIN lang 6-seitig oder 4-seitig,
wir sind für alle Vorschläge offen.
Wir sind eine Umzugsfirma für Privatumzüge, Firmenumzüge und Personaldienstleistung und kümmern uns um alles was in einem Umzug anfällt bzw. verpacken der Möbel Auf und Abbau der Möbel, Einpackservice aller Haushaltsgegenstände, darüber hinaus stellen wir auch nur Umzugshelfer.
Montage von Neumöbel wie Wandbrook durch geschultes Personal.
Die Infos wie z.B E-Mail, und Telefon sollten auch auf das Produkt.
E-Mail : info@pkv-transporte.example
Tel. 0049 152 38847261
Adresse: Lerchenfeldweg 27
74829 Feldhausen an der Murr
Der Tex sollte noch enthalten:
Über uns:
PKV Transporte ist ein erfahrenes und kompetentes Umzugsunternehmen aus Feldhausen.
Innerhalb der Umzugsbranche reduzieren wir uns nicht nur auf Privatumzüge, den unsere Palette reicht vom Firmenumzug, Entrümpelung und Ankauf von gebrauchte Büromöbeln so wie Personaldienstleistung in der Möbelbrache.
Wir bieten Ihnen:
-TOP Qualität zu fairen Preisen
-Wissen aus jahrelanger Erfahrung
-persönliche Beratung von der Idee bis zum Umzug
-ausgebildete Fachkräfte für Montagearbeiten, Entrümpelung, Ein- und Auspackservice das alles mit den Modernsten und besten Werkzeugen.
-Terminsicherheit auch bei kurzfristigem Umzugswunsch
-Einen verlässlichen Umzugspartner
Privatumzüge:
Sie freuen sich auf Ihre neuen vier Wände.
Vorher steht eine Menge Arbeit ins Haus: Ihr Umzug.
Kein Problem, wir packen das für Sie an.
PKV Transporte macht Ihren Möbeln Beine !
Unser Leistungsspektrum umfasst alle Dienstleistungen rund um Ihren Umzug aus einer Hand:
Wir packen ein und aus, demontieren und montieren sämtliche Möbel,
leisten fachgerechte Schreiner-, Elektro- und Installationsarbeiten.
Bei uns sind Sie auf der sicheren Seite !
Es wird alles zu einem Festpreis..
Aufgabenstellung
Wir möchten das der Text Modern, kurz und knackig ist , darf auch etwas aus der reihe tanzen

```html
<!DOCTYPE html>
<html lang="de">
<head>
<meta charset="utf-8">
<title>PKV Transporte – Falzflyer DIN lang</title>
<link href="https://fonts.googleapis.com/css2?family=Montserrat:ital,wght@0,300;0,400;0,600;0,700;0,800;1,300;1,400;1,600&display=swap" rel="stylesheet">
<style>
:root{
  --slate:#55657e;
  --slate-dark:#46556c;
  --orange:#f07c1c;
  --text:#6b7383;
  --paper:#ffffff;
  --bg:#eceef1;
  --photo-a:#c9b49a;
  --photo-b:#6d7f9c;
}
*{box-sizing:border-box;margin:0;padding:0}
html,body{width:1200px;height:2286px;overflow:hidden}
body{background:var(--bg);font-family:"Montserrat",sans-serif;color:var(--slate);position:relative}
.sheet{position:absolute;left:60px;width:1080px;height:764px;display:flex;background:var(--paper);box-shadow:0 18px 40px rgba(40,50,70,.18)}
.sheet--inside{top:200px}
.sheet--outside{top:1250px}
.panel{position:relative;width:360px;height:100%;overflow:hidden}
.panel + .panel{border-left:1px solid #eef0f3}
.heading{font-weight:800;font-size:24px;letter-spacing:.5px;text-transform:uppercase;line-height:1.05;color:var(--slate)}
.rule{height:2px;background:var(--orange)}
.copy{font-style:italic;font-weight:300;font-size:12.5px;line-height:1.35;color:var(--text)}
.copy strong{font-weight:600;color:var(--slate)}
.copy .accent{font-weight:600;color:var(--orange)}
.url{font-weight:700;font-size:17px;color:var(--orange);text-align:center;white-space:nowrap}
.url-line{display:flex;align-items:center;gap:10px}
.url-line::before,.url-line::after{content:"";flex:1;height:1.5px;background:var(--orange)}

/* inside, panel 1 */
.offers{padding:40px 28px 0 40px}
.offers::before{content:"";position:absolute;left:0;top:0;bottom:0;width:12px;background:var(--slate)}
.offers .heading{margin-bottom:14px}
.offer{display:flex;gap:12px;padding:14px 0;border-top:1.5px solid var(--orange)}
.offer:first-of-type{border-top:2px solid var(--orange)}
.offer svg{flex:none}
.offer-title{font-weight:700;font-size:12.5px;color:var(--orange);text-transform:uppercase}
.offer-text{font-weight:700;font-size:12.5px;color:var(--slate);line-height:1.3}
.ticks{list-style:none;margin:5px 0 4px}
.ticks li{display:flex;align-items:center;gap:6px;font-weight:600;font-size:12px;line-height:1.6}
.offer-note{font-weight:700;font-size:12px;margin-left:18px;line-height:1.3}
.contact{position:absolute;left:40px;right:28px;bottom:34px;text-align:center}
.contact-label{font-weight:700;font-size:14px;letter-spacing:.5px;margin-bottom:8px}

/* photo + badge */
.photo{position:relative;height:310px;background:linear-gradient(135deg,var(--photo-a),var(--photo-b))}
.photo--cool{background:linear-gradient(160deg,#a9c3dc,#5a6e8e 70%,#c2a47e)}
.photo-curve{position:absolute;left:0;bottom:-1px;width:360px;height:80px}
.badge{position:absolute;left:56px;bottom:-22px;width:104px;height:104px;border-radius:50%;background:var(--slate);border:5px solid #fff;box-shadow:0 0 0 2px var(--slate);color:#fff;text-align:center;padding-top:14px;z-index:2}
.badge small{display:block;font-size:8px;letter-spacing:1.5px;font-weight:400;margin-top:2px}
.badge b{display:block;font-size:14px;line-height:1.1;font-weight:700}

/* inside, panel 2 */
.service-body{padding:44px 30px 0}
.service-body .heading{margin-bottom:10px}
.service-body .rule{margin-bottom:14px}
.service-body .copy p{margin-bottom:12px}
.service-body .heading + .rule + .copy{margin-bottom:22px}

/* inside, panel 3 */
.private{padding:40px 28px 0 30px}
.private::before{content:"";position:absolute;left:30px;right:0;top:26px;height:4px;background:var(--slate)}
.private .heading{margin:6px 0 16px;font-size:23px}
.private .copy p{margin-bottom:11px}

/* outside, panel 1 */
.about-body{padding:48px 30px 0}
.about-body .heading{font-size:27px;margin-bottom:10px}
.about-body .rule{margin-bottom:16px}
.about-body .copy{font-size:13.5px}
.about-body .copy p{margin-bottom:14px}
.about .url-line{position:absolute;left:30px;right:30px;bottom:34px}
.top-band{position:absolute;left:0;right:0;top:0;height:8px;background:var(--orange);z-index:3}

/* outside, panel 2 */
.contact-panel{background:var(--slate);color:#fff;padding:120px 30px 0;text-align:center}
.brand-name{font-weight:800;font-size:26px;letter-spacing:1px;line-height:1;text-transform:uppercase;white-space:nowrap}
.brand-sub{font-weight:600;font-size:9px;letter-spacing:1.5px;margin-top:6px;text-transform:uppercase;opacity:.9}
.contact-row{margin-top:34px}
.contact-icon{display:flex;align-items:center;gap:10px}
.contact-icon::before,.contact-icon::after{content:"";flex:1;height:1px;background:rgba(255,255,255,.7)}
.contact-text{font-weight:400;font-size:14px;line-height:1.35;margin-top:10px}
.contact-url{font-weight:600;font-size:14.5px;letter-spacing:.5px;margin-top:44px;padding-top:14px;border-top:1px solid rgba(255,255,255,.7);white-space:nowrap}

/* outside, panel 3 */
.cover-head{height:140px;padding:44px 24px 0;text-align:center}
.cover-head::before{content:"";position:absolute;right:0;top:0;width:210px;height:10px;background:var(--orange)}
.cover-head .brand-name{color:var(--slate);font-size:28px}
.cover-head .brand-sub{color:var(--orange);opacity:1}
.cover .photo{height:360px}
.cover-title{padding:46px 24px 0;text-align:center}
.cover-title .heading{font-size:28px}
.cover-title .sub{font-weight:800;font-size:21px;text-transform:uppercase}
.cover .url-line{position:absolute;left:24px;right:24px;bottom:34px}
</style>
</head>
<body>

<section class="sheet sheet--inside">

  <div class="panel offers">
    <h2 class="heading">Wir bieten Ihnen</h2>

    <div class="offer">
      <svg width="26" height="26" viewBox="0 0 26 26"><circle cx="13" cy="13" r="11.5" fill="none" stroke="#f07c1c" stroke-width="2"/><path d="M13 6l2 4.3 4.6.6-3.4 3.2.9 4.6-4.1-2.3-4.1 2.3.9-4.6-3.4-3.2 4.6-.6z" fill="#55657e"/></svg>
      <div><div class="offer-title">TOP Qualität</div><div class="offer-text">zu fairen Preisen.</div></div>
    </div>
    <div class="offer">
      <svg width="26" height="26" viewBox="0 0 26 26"><circle cx="13" cy="13" r="11.5" fill="none" stroke="#f07c1c" stroke-width="2"/><path d="M13 6a5 5 0 0 0-3 9v2h6v-2a5 5 0 0 0-3-9zM10.5 18.5h5v1.5h-5z" fill="#55657e"/></svg>
      <div><div class="offer-title">Wissen</div><div class="offer-text">aus jahrelanger Erfahrung.</div></div>
    </div>
    <div class="offer">
      <svg width="26" height="26" viewBox="0 0 26 26"><circle cx="13" cy="13" r="11.5" fill="none" stroke="#f07c1c" stroke-width="2"/><path d="M7 8h12v7h-6l-3 3v-3H7z" fill="#55657e"/></svg>
      <div><div class="offer-title">Persönliche Beratung</div><div class="offer-text">von der Idee bis zum Umzug.</div></div>
    </div>
    <div class="offer">
      <svg width="26" height="26" viewBox="0 0 26 26"><circle cx="13" cy="13" r="11.5" fill="none" stroke="#f07c1c" stroke-width="2"/><path d="M7 16a6 6 0 0 1 12 0zM6 16.5h14v1.8H6z" fill="#55657e"/></svg>
      <div>
        <div class="offer-title">Ausgebildete Fachkräfte</div>
        <div class="offer-text">für:</div>
        <ul class="ticks">
          <li><svg width="11" height="11" viewBox="0 0 12 12"><circle cx="6" cy="6" r="5" fill="none" stroke="#f07c1c" stroke-width="1.4"/><path d="M3.5 6l1.8 1.8L8.6 4.4" fill="none" stroke="#f07c1c" stroke-width="1.4"/></svg>Montagearbeiten</li>
          <li><svg width="11" height="11" viewBox="0 0 12 12"><circle cx="6" cy="6" r="5" fill="none" stroke="#f07c1c" stroke-width="1.4"/><path d="M3.5 6l1.8 1.8L8.6 4.4" fill="none" stroke="#f07c1c" stroke-width="1.4"/></svg>Entrümpelung</li>
          <li><svg width="11" height="11" viewBox="0 0 12 12"><circle cx="6" cy="6" r="5" fill="none" stroke="#f07c1c" stroke-width="1.4"/><path d="M3.5 6l1.8 1.8L8.6 4.4" fill="none" stroke="#f07c1c" stroke-width="1.4"/></svg>Ein- und Auspackservice</li>
        </ul>
        <div class="offer-note">Das alles mit den modernsten und besten Werkzeugen.</div>
      </div>
    </div>
    <div class="offer">
      <svg width="26" height="26" viewBox="0 0 26 26"><circle cx="13" cy="13" r="11.5" fill="none" stroke="#f07c1c" stroke-width="2"/><path d="M8 12h3v7H8zM12 19v-7l3-5c1.5 0 2 1 1.6 2.4L16 12h3.5c1 0 1.5.8 1.2 1.7l-1.6 4.5c-.3.6-.8.8-1.4.8z" fill="#55657e"/></svg>
      <div><div class="offer-title">Zuverlässigkeit</div><div class="offer-text">einen verlässlichen Umzugspartner.</div></div>
    </div>

    <div class="contact">
      <div class="contact-label">KONTAKTIEREN SIE UNS:</div>
      <div class="url url-line">www.pkv-transporte.example</div>
    </div>
  </div>

  <div class="panel service">
    <div class="photo" role="img" aria-label="Foto: lächelnder Umzugshelfer trägt Kartons vor einem Wohnhaus">
      <svg class="photo-curve" viewBox="0 0 360 80" preserveAspectRatio="none"><path d="M0 80V52Q180 -10 360 40V80z" fill="#fff"/><path d="M0 70Q30 34 80 28" fill="none" stroke="#f07c1c" stroke-width="7"/></svg>
      <div class="badge">
        <svg width="14" height="14" viewBox="0 0 24 24"><path d="M6.6 10.8a15 15 0 0 0 6.6 6.6l2.2-2.2c.3-.3.7-.4 1-.2 1.1.4 2.3.6 3.6.6.6 0 1 .4 1 1V20c0 .6-.4 1-1 1A17 17 0 0 1 3 4c0-.6.4-1 1-1h3.5c.6 0 1 .4 1 1 0 1.3.2 2.5.6 3.6.1.3 0 .7-.2 1z" fill="#fff"/></svg>
        <small>ANRUFEN</small><b>0152 388</b><b>47261</b>
      </div>
    </div>
    <div class="service-body">
      <h2 class="heading">Ein- und Auspack<br>Service</h2>
      <div class="rule"></div>
      <div class="copy">
        <p>Haben Sie bei Ihrem Umzug Angst um Ihr Porzellan oder Geschirr?</p>
        <p>Lassen Sie es doch einfach durch unsere Umzugsprofis einpacken und auspacken, damit auch nichts zu Bruch geht.</p>
      </div>
      <h2 class="heading">Versicherung</h2>
      <div class="rule"></div>
      <div class="copy">
        <p>In alle unseren Angeboten ist selbstverständlich eine Transport- und Haftpflichtversicherung kostenlos enthalten</p>
      </div>
    </div>
  </div>

  <div class="panel private">
    <h2 class="heading">Privatumzüge</h2>
    <div class="copy">
      <p><strong>Sie freuen sich auf Ihre neuen vier Wände.</strong></p>
      <p>Vorher steht eine Menge Arbeit ins Haus: Ihr Umzug.</p>
      <p><strong>Kein Problem, wir packen das für Sie an.</strong></p>
      <p class="accent">PKV Transporte macht Ihren Möbeln Beine!</p>
      <p>Unser Leistungsspektrum umfasst alle Dienstleistungen rund um Ihren Umzug aus einer Hand:</p>
      <p>Wir packen ein und aus, demontieren und montieren sämtliche Möbel, leisten fachgerechte Schreiner-, Elektro- und Installationsarbeiten.</p>
      <p class="accent">Bei uns sind Sie auf der sicheren Seite!</p>
      <p>Es wird alles zu einem Festpreis angeboten, nicht wie bei anderen Unternehmen, wo Sie am Ende noch mit zusatzkosten rechnen müssen.</p>
      <p><strong>In unserem Festpreis ist enthalten:</strong></p>
      <p>die Versicherung des Umzugsgutes, der/des Wohnung/Hauses. Schutzdecken für die Möbel sowie Gurte und Verpackungsmaterial, ausgenommen Umzugskartons.</p>
    </div>
  </div>
</section>

<section class="sheet sheet--outside">

  <div class="panel about">
    <div class="top-band"></div>
    <div class="photo photo--cool" role="img" aria-label="Foto: Umzugshelfer mit Karton vor einem Transporter unter blauem Himmel">
      <svg class="photo-curve" viewBox="0 0 360 80" preserveAspectRatio="none"><path d="M0 80V52Q180 -10 360 40V80z" fill="#fff"/><path d="M0 70Q30 34 80 28" fill="none" stroke="#f07c1c" stroke-width="7"/></svg>
      <div class="badge">
        <svg width="14" height="14" viewBox="0 0 24 24"><path d="M6.6 10.8a15 15 0 0 0 6.6 6.6l2.2-2.2c.3-.3.7-.4 1-.2 1.1.4 2.3.6 3.6.6.6 0 1 .4 1 1V20c0 .6-.4 1-1 1A17 17 0 0 1 3 4c0-.6.4-1 1-1h3.5c.6 0 1 .4 1 1 0 1.3.2 2.5.6 3.6.1.3 0 .7-.2 1z" fill="#fff"/></svg>
        <small>ANRUFEN</small><b>0152 388</b><b>47261</b>
      </div>
    </div>
    <div class="about-body">
      <h2 class="heading">Über uns</h2>
      <div class="rule"></div>
      <div class="copy">
        <p>PKV Transporte ist ein erfahrenes und kompetentes Umzugsunternehmen aus Feldhausen.</p>
        <p>Innerhalb der Umzugsbranche reduzieren wir uns nicht nur auf Privatumzüge, den unsere Palette reicht vom Firmenumzug, Entrümpelung und Ankauf von gebrauchte Büromöbeln so wie Personaldienstleistung in der Möbelbrache.</p>
      </div>
    </div>
    <div class="url url-line">www.pkv-transporte.example</div>
  </div>

  <div class="panel contact-panel">
    <div class="brand-name">PKV Transporte</div>
    <div class="brand-sub">Möbeltransport und Dienstleister</div>

    <div class="contact-row">
      <div class="contact-icon"><svg width="24" height="24" viewBox="0 0 24 24"><circle cx="12" cy="12" r="11" fill="none" stroke="#fff" stroke-width="1.4"/><path d="M12 6a4 4 0 0 0-4 4c0 3 4 8 4 8s4-5 4-8a4 4 0 0 0-4-4zm0 5.5a1.5 1.5 0 1 1 0-3 1.5 1.5 0 0 1 0 3z" fill="#fff"/></svg></div>
      <div class="contact-text">Lerchenfeldweg 27<br>74829 Feldhausen an der Murr</div>
    </div>
    <div class="contact-row">
      <div class="contact-icon"><svg width="24" height="24" viewBox="0 0 24 24"><circle cx="12" cy="12" r="11" fill="none" stroke="#fff" stroke-width="1.4"/><path d="M9 7.5l1.6 2.4-1 1.2a7 7 0 0 0 3.3 3.3l1.2-1 2.4 1.6-.8 1.8c-4 .2-8.4-4.2-8.2-8.2z" fill="#fff"/></svg></div>
      <div class="contact-text">0049 152 38847261</div>
    </div>
    <div class="contact-row">
      <div class="contact-icon"><svg width="24" height="24" viewBox="0 0 24 24"><circle cx="12" cy="12" r="11" fill="none" stroke="#fff" stroke-width="1.4"/><path d="M6.5 8.5h11v7h-11z" fill="none" stroke="#fff" stroke-width="1.3"/><path d="M6.5 8.5l5.5 4 5.5-4" fill="none" stroke="#fff" stroke-width="1.3"/></svg></div>
      <div class="contact-text">info@pkv-transporte.example</div>
    </div>
    <div class="contact-url">WWW.PKV-TRANSPORTE.EXAMPLE</div>
  </div>

  <div class="panel cover">
    <div class="cover-head">
      <div class="brand-name">PKV Transporte</div>
      <div class="brand-sub">Möbeltransport und Dienstleister</div>
    </div>
    <div class="photo" role="img" aria-label="Foto: zwei Umzugshelfer in Latzhosen tragen Kartons vor einem Transporter">
      <svg class="photo-curve" viewBox="0 0 360 80" preserveAspectRatio="none"><path d="M0 80V52Q180 -10 360 40V80z" fill="#fff"/><path d="M0 70Q30 34 80 28" fill="none" stroke="#f07c1c" stroke-width="7"/></svg>
      <div class="badge">
        <svg width="14" height="14" viewBox="0 0 24 24"><path d="M6.6 10.8a15 15 0 0 0 6.6 6.6l2.2-2.2c.3-.3.7-.4 1-.2 1.1.4 2.3.6 3.6.6.6 0 1 .4 1 1V20c0 .6-.4 1-1 1A17 17 0 0 1 3 4c0-.6.4-1 1-1h3.5c.6 0 1 .4 1 1 0 1.3.2 2.5.6 3.6.1.3 0 .7-.2 1z" fill="#fff"/></svg>
        <small>ANRUFEN</small><b>0152 388</b><b>47261</b>
      </div>
    </div>
    <div class="cover-title">
      <h1 class="heading">Ihr Profi für</h1>
      <div class="sub">Umzüge aller Art</div>
    </div>
    <div class="url url-line">www.pkv-transporte.example</div>
  </div>
</section>

</body>
</html>
```